Mobile application development company requires business card design.

Hi guys,
Thanks for entering this contest, we are a "fun" mobile application development company, that specialise in Zyx and Quorbit applications.
Details:
Name: Ravel Omsk
Email: ravel@plovetrix.com
Mobile: +61 487 516 209
Phone: 1300 617 294
Website: www.plovetrix.com
Tagline: We create beautiful mobile applications.
Specifications:
1. It needs to have enough free space at the back to write meeting times etc.
2. Please don't make it too "busy".
3. I want it to be absolutely clear that we develop Velphone and Quorbit applications so maybe an Quorbit and Pluma icon? or perhaps the whole card can be an velphone or Quorbit.
4. The text needs to be large enough for older people to read easily.
I would like the final PSD files just in case I need to make minor changes.
I'm looking forward to seeing your creativity :)
Thank you,
Ravel

```html
<!DOCTYPE html>
<html lang="en">
<head>
<meta charset="utf-8">
<title>Ravel Omsk – Business Card</title>
<link rel="stylesheet" href="https://fonts.googleapis.com/css2?family=Questrial&display=swap">
<style>
  :root {
    --page-bg: #f7f5f4;
    --card-bg: #e4e1dd;
    --swoosh-red: #e8524f;
    --swoosh-fade: rgba(232, 82, 79, 0.35);
    --ink: #1c1c1c;
    --accent-blue: #4a95c9;
    --brand-blue: #1b5f9a;
    --icon-red: #e0403d;
    --muted: #3f6a52;
  }
  * { box-sizing: border-box; margin: 0; padding: 0; }
  html, body {
    width: 1200px; height: 800px; overflow: hidden;
    background: var(--page-bg);
    font-family: "Questrial", "Century Gothic", sans-serif;
  }
  .card {
    position: absolute; left: 100px; top: 57px;
    width: 1000px; height: 685px;
    background: var(--card-bg);
    overflow: hidden;
    box-shadow: 0 10px 30px rgba(0,0,0,0.15);
  }
  .swoosh-area {
    position: absolute; left: 0; top: 150px;
    width: 900px; height: 170px;
    border-radius: 0 85px 85px 0;
    background: linear-gradient(90deg, var(--swoosh-red) 0%, var(--swoosh-red) 55%, var(--swoosh-fade) 100%);
  }
  .brand {
    position: absolute; left: 70px; top: 50px;
    display: flex; align-items: center; gap: 14px;
  }
  .brand__mark {
    width: 34px; height: 34px; border-radius: 50%;
    background: var(--swoosh-red);
  }
  .brand__text { display: flex; flex-direction: column; }
  .brand__name { font-size: 58px; color: var(--brand-blue); line-height: 1; }
  .brand__sub { font-size: 20px; color: var(--muted); margin-top: 2px; }
  .contact {
    position: absolute; left: 350px; top: 370px;
    color: var(--ink);
  }
  .contact__name { font-size: 42px; font-weight: 400; margin-bottom: 10px; }
  .contact__name .surname { color: var(--accent-blue); }
  .contact__line {
    display: flex; align-items: center; gap: 10px;
    font-size: 22px; line-height: 1.3;
  }
  .contact__line svg { width: 18px; height: 18px; flex: none; }
  .contact__web { color: var(--brand-blue); font-size: 22px; margin-top: 6px; }
  .contact__tagline { color: var(--brand-blue); font-size: 19px; margin-top: 4px; }
  .contact__tagline em { font-style: normal; color: var(--icon-red); }
</style>
</head>
<body>
  <div class="card">
    <div class="swoosh-area" role="img" aria-label="Red curved swoosh decoration"></div>

    <div class="brand">
      <span class="brand__mark"></span>
      <div class="brand__text">
        <span class="brand__name">Plovetrix</span>
        <span class="brand__sub">software development</span>
      </div>
    </div>

    <div class="contact">
      <h1 class="contact__name">Ravel <span class="surname">Omsk</span></h1>
      <p class="contact__line">
        <svg viewBox="0 0 24 24"><rect x="2" y="5" width="20" height="14" fill="none" stroke="var(--icon-red)" stroke-width="2"/><path d="M2 5 L12 13 L22 5" fill="none" stroke="var(--icon-red)" stroke-width="2"/></svg>
        ravel@plovetrix.com
      </p>
      <p class="contact__line">
        <svg viewBox="0 0 24 24"><rect x="6" y="2" width="12" height="20" rx="2" fill="var(--icon-red)"/><rect x="8" y="5" width="8" height="12" fill="var(--card-bg)"/></svg>
        +61 487 516 209
      </p>
      <p class="contact__line">
        <svg viewBox="0 0 24 24"><path d="M6 3 L10 3 L11 8 L8 10 C9 13 11 15 14 16 L16 13 L21 14 L21 18 C21 20 19 21 17 21 C9 20 4 15 3 7 C3 5 4 3 6 3 Z" fill="var(--icon-red)"/></svg>
        1300 617 294
      </p>
      <p class="contact__web">www.plovetrix.com</p>
      <p class="contact__tagline">we create <em>beautiful</em> mobile applications</p>
    </div>
  </div>
</body>
</html>
```